Career development coaching - school lever to adults, needs a business card

Tandem Lark - An independent Career Advice business that provides 1-2-1 advice,for career development, entrepreneurial support and workshops needs a business card. Our clients of all ages (school leaver to adults looking for a career move) and universities and colleges. We would like the card to be double-sided with a modern, professional look. Looking for something professional yet very creative and original. Want a standard size business card that inspires a second look because it stands out from the rest.

One side of the card to have a design incorporating the logo with Tandem Lark name with the strap line “Helping you find your future” and space for the company website

Other side of the card to the logo/Tandem Lark name and the usual contact information:
Individual Name
Job Title (for example, Director)
Phone number
Email address
Company website address

Facebook, LinkedIn and Twitter links will need to go somewhere (back or front!)

The design will be used for 3 individuals so should be editable so that we can update as needed/as we grow.

Attached is the company logo/colours to be incorporated.

Target Market(s)

1-2-1 advice,for career development, entrepreneurial support and workshops needs a business card. Our clients of all ages (school leaver to adults looking for a career move) and universities and colleges.

Industry/Entity Type

Consulting

Contact Information for Business Card

Individual Name
Phone number
Email address
Company website address

Font styles to use
Sans Serif

Colors
0255a3
3176b5
faa54b
f78f20
85acd3
cfdeed

Requirements
Must have
• use the Tandem Lark Logo in some way - using the colours and the blue/orange palette
• For the logo - hope this makes sense to someone or if they direclty relate to the logo image attached!
• For the Orange:- Pantone 1585 C
• In CMYK : C3 M71 Y100 K0
• For the Blue:- 100% Pantone 7469 C
• In CMYK : C100 M62 Y27 K7
• Please feel free to contact me with any questions for more info
Nice to have
• happy to see any creative designs
Should not have
• Nothing too traditional,

```html
<!DOCTYPE html>
<html lang="en">
<head>
<meta charset="utf-8">
<title>Tandem Lark — Business Card</title>
<link rel="stylesheet" href="https://fonts.googleapis.com/css2?family=Open+Sans:wght@400;600;700&display=swap">
<style>
  :root {
    --backdrop: #8e9092;
    --card-white: #eceef1;
    --brand-blue: #0f5a80;
    --brand-orange: #e2692b;
    --ink-grey: #4f5358;
    --tag-grey: #5d6166;
    --mark-light: #e4e7eb;
  }
  * { margin: 0; padding: 0; box-sizing: border-box; }
  html, body {
    width: 1105px;
    height: 1200px;
    overflow: hidden;
    background: var(--backdrop);
    font-family: "Open Sans", Arial, sans-serif;
  }
  .card {
    position: absolute;
    left: 172px;
    width: 760px;
    height: 436px;
  }
  .card--front { top: 110px; background: var(--card-white); }
  .card--back  { top: 654px; background: var(--brand-blue); }

  .brand-dot {
    position: absolute;
    left: 134px;
    top: 62px;
    width: 96px;
    height: 96px;
    border-radius: 50%;
    background: var(--brand-orange);
  }
  .brand-name {
    position: absolute;
    left: 62px;
    top: 188px;
    font-size: 32px;
    font-weight: 600;
    letter-spacing: 1px;
    color: var(--brand-blue);
    line-height: 1;
  }
  .tagline {
    position: absolute;
    left: 62px;
    top: 230px;
    font-size: 13px;
    font-weight: 400;
    letter-spacing: 0.3px;
    color: var(--tag-grey);
    text-transform: uppercase;
  }
  .contact-list {
    position: absolute;
    left: 62px;
    top: 298px;
    list-style: none;
  }
  .contact-list li {
    display: flex;
    align-items: center;
    height: 28px;
    font-size: 19px;
    color: var(--ink-grey);
  }
  .contact-list svg {
    width: 18px;
    height: 18px;
    margin-right: 14px;
    fill: var(--brand-blue);
  }
  .person {
    position: absolute;
    right: 62px;
    top: 310px;
    text-align: right;
  }
  .person-name {
    font-size: 28px;
    font-weight: 600;
    color: var(--brand-blue);
    line-height: 1.1;
  }
  .person-title {
    font-size: 19px;
    color: var(--brand-orange);
    letter-spacing: 0.5px;
    line-height: 1.4;
  }

  .back-name {
    position: absolute;
    left: 0;
    width: 100%;
    top: 160px;
    text-align: center;
    font-size: 58px;
    font-weight: 600;
    letter-spacing: 1px;
    color: var(--mark-light);
    line-height: 1;
  }
  .social-row {
    position: absolute;
    left: 0;
    width: 100%;
    top: 345px;
    display: flex;
    justify-content: center;
    gap: 8px;
  }
  .social-dot {
    width: 44px;
    height: 44px;
    border-radius: 50%;
    background: var(--mark-light);
  }
</style>
</head>
<body>
  <section class="card card--front">
    <div class="brand-dot"></div>
    <div class="brand-name">Tandem Lark</div>
    <div class="tagline">Helping you find your future</div>

    <ul class="contact-list">
      <li>
        <svg viewBox="0 0 24 24" aria-hidden="true"><path d="M6.6 10.8a15.1 15.1 0 0 0 6.6 6.6l2.2-2.2a1 1 0 0 1 1-.25 11.4 11.4 0 0 0 3.6.57 1 1 0 0 1 1 1V20a1 1 0 0 1-1 1A17 17 0 0 1 3 4a1 1 0 0 1 1-1h3.5a1 1 0 0 1 1 1c0 1.25.2 2.45.57 3.6a1 1 0 0 1-.25 1z"/></svg>
        555 0142 7789
      </li>
      <li>
        <svg viewBox="0 0 24 24" aria-hidden="true"><path d="M2 5h20v2l-10 6L2 7z M2 9l10 6 10-6v10H2z"/></svg>
        rowan@tandemlark.com
      </li>
      <li>
        <svg viewBox="0 0 24 24" aria-hidden="true"><path d="M12 2a10 10 0 1 0 0 20 10 10 0 0 0 0-20zm-1 17.9A8 8 0 0 1 4.1 11H8l3 3zm6.9-2.4A2 2 0 0 0 16 16h-1v-3l-4-4H8V7h2l2-2h2a8 8 0 0 1 3.9 12.5z"/></svg>
        www.tandemlark.com
      </li>
    </ul>

    <div class="person">
      <div class="person-name">ROWAN PELL</div>
      <div class="person-title">PRESIDENT</div>
    </div>
  </section>

  <section class="card card--back">
    <div class="back-name">Tandem Lark</div>
    <div class="social-row" aria-label="Social links">
      <span class="social-dot"></span>
      <span class="social-dot"></span>
      <span class="social-dot"></span>
    </div>
  </section>
</body>
</html>
```